Business Card & Logo Design

Originally the brief was for a card only - I now think it's probably better to include a logo design as well. PLease add $200 to the Budget of $210, Apologies for the inconvenience for thaos that have already submitted designs.

Lantern Hollow Productions Pty Ltd is a video/dvd/ production company. Primarily corporate medium to high end. It's a one man operation that's been in business 20 years.

The name " Lantern Hollow" is a primarily a reference to Mathieu Corbelle film that's about film making. Shooting "Lantern Hollow" is also a technique employed by cinematographers to make scenes shot in daylight look like night.

See the design emphasising blue day/night tones but open to other ideas.

Main Text can either be Lantern Hollow Productions or Lantern Hollow.

Many thanks to all designers who submitted ideas for this brief.

Choosing between the designs was very difficult indeed.

I wish everyone the best and may the next job be yours!

Warren

• Text for card:
In Larger Print
Lantern Hollow Productions or Lantern Hollow
Warren Bellamy
In Smaller Print
Lantern Hollow Productions Pty Ltd.
17 Pelham Street
Marlow Vale, VIC, 3188
P: 9734 2061
m: 0438 725 190
e: warrenbellamy@ostrafel.com

```html
<!DOCTYPE html>
<html lang="en">
<head>
<meta charset="utf-8">
<title>Lantern Hollow Productions – Business Card</title>
<link rel="stylesheet" href="https://fonts.googleapis.com/css2?family=Questrial&display=swap">
<style>
  :root {
    --page: #ffffff;
    --card: #ffffff;
    --card-edge: #dcdcdc;
    --ink: #1b1f74;
    --accent: #3040ee;
    --rule: #a3a3a3;
  }
  html, body {
    margin: 0;
    padding: 0;
    width: 1200px;
    height: 442px;
    overflow: hidden;
    background: var(--page);
  }
  .canvas {
    position: relative;
    width: 1200px;
    height: 442px;
    font-family: "Questrial", "Century Gothic", sans-serif;
    color: var(--ink);
  }
  .card {
    position: absolute;
    top: 60px;
    width: 558px;
    height: 317px;
    background: var(--card);
    border: 2px solid var(--card-edge);
    border-radius: 28px;
  }
  .card--front { left: 17px; }
  .card--back { left: 621px; }

  .brand-mark {
    position: absolute;
    border-radius: 50%;
    background: var(--accent);
  }
  .card--front .brand-mark {
    left: 286px;
    top: 135px;
    width: 84px;
    height: 84px;
  }
  .card--front .brand-name {
    position: absolute;
    left: 96px;
    top: 236px;
    margin: 0;
    font-size: 27px;
    font-weight: 400;
    letter-spacing: 0.5px;
    white-space: nowrap;
  }

  .card--back .brand-mark {
    left: 284px;
    top: 40px;
    width: 30px;
    height: 30px;
  }
  .card--back .brand-name {
    position: absolute;
    left: 0;
    width: 100%;
    top: 80px;
    margin: 0;
    text-align: center;
    font-size: 12px;
    font-weight: 400;
    white-space: nowrap;
  }
  .divider {
    position: absolute;
    left: 44px;
    right: 44px;
    top: 98px;
    height: 0;
    border-top: 1.5px solid var(--rule);
  }
  .person-name {
    position: absolute;
    left: 0;
    width: 100%;
    top: 130px;
    margin: 0;
    text-align: center;
    font-size: 24px;
    font-weight: 400;
    letter-spacing: 0.3px;
  }
  .contact {
    position: absolute;
    left: 0;
    width: 100%;
    top: 191px;
    margin: 0;
    text-align: center;
    font-style: normal;
    font-size: 12.5px;
    line-height: 16px;
  }
</style>
</head>
<body>
  <main class="canvas">
    <section class="card card--front" aria-label="Card front">
      <span class="brand-mark" aria-hidden="true"></span>
      <h1 class="brand-name">Lantern Hollow Productions</h1>
    </section>

    <section class="card card--back" aria-label="Card back">
      <span class="brand-mark" aria-hidden="true"></span>
      <p class="brand-name">Lantern Hollow Productions</p>
      <div class="divider"></div>
      <h2 class="person-name">Warren Bellamy</h2>
      <address class="contact">
        17 Pelham Street<br>
        Marlow Vale, VIC, 3188<br>
        P: 9734 2061<br>
        M: 0438 725 190<br>
        E: warrenbellamy@ostrafel.com
      </address>
    </section>
  </main>
</body>
</html>
```